Brisk Refrigeration. Refrigeration and air conditioning specialists.

We need a website to promote our business. We would a modern simple design using the colours from our logo and black. We want it to be fun but proffesional.

Target Market(s)

Commercial

Number of Pages Required

4 page

Requirements
Must have
• Home Page, About Us, Services and Contact Us.
• 24/7 365 days service available.
• Brisk Refrigeration's dedicated team specialises in commercial refrigeration and air conditioning equipment.
• Based in Joondalup, we cover Perth Metro and surrounding areas.
Nice to have
• KNOWLEDGE . EXPERIENCE . PASSION in bold.
• Our experienced and highly trained technicians provide extensive knowledge and exceptional skills for your commercial refrigeration and air conditioning requirements.
• Pictures of commercial refrigeration.
Should not have
• No mention of domestic services.

```html
<!DOCTYPE html>
<html lang="en">
<head>
<meta charset="utf-8">
<title>Brisk Refrigeration</title>
<link rel="stylesheet" href="https://fonts.googleapis.com/css2?family=Raleway:wght@400;500;600;700&display=swap">
<style>
:root{
  --lime:#9be55a;
  --lime-soft:#a8e672;
  --ink:#131217;
  --ink-deep:#0e0d12;
  --paper:#eeeef1;
  --text-dark:#2b2b2f;
  --white:#ffffff;
  --navy:#2e2c40;
  --field:#d6d6dc;
  --violet:#7e6f9f;
  --bar:#2b2b2e;
  --muted:#9a9aa2;
}
*{box-sizing:border-box;margin:0;padding:0}
html,body{width:1200px;height:2647px;overflow:hidden}
body{position:relative;font-family:"Raleway",sans-serif;background:var(--paper);color:var(--text-dark)}
.abs{position:absolute}

/* Hero */
.hero{position:absolute;left:0;top:0;width:1200px;height:577px;
  background:linear-gradient(100deg,#2f3a3c 0%,#4a5656 35%,#5d5e54 55%,#8a5a33 75%,#3c3a35 100%)}
.hero-shade{position:absolute;inset:0;background:linear-gradient(90deg,rgba(10,14,16,.55) 0%,rgba(10,14,16,.2) 55%,rgba(10,14,16,0) 100%)}
.topbar{position:absolute;left:0;top:0;width:1200px;height:120px;background:rgba(40,44,46,.55)}
.brand{position:absolute;font-family:"Raleway",sans-serif;font-weight:700;color:var(--lime);letter-spacing:1px}
.brand-top{left:212px;top:28px;font-size:44px;line-height:48px}
.nav{position:absolute;display:flex;font-size:17px;color:var(--white)}
.nav-top{left:656px;top:50px;gap:0}
.nav a{color:inherit;text-decoration:none;position:absolute;white-space:nowrap}
.hero-title{position:absolute;left:229px;top:218px;font-size:35px;line-height:53px;font-weight:500;color:var(--white);letter-spacing:1px}
.hero-title .accent{color:var(--lime)}
.hero-copy{position:absolute;left:229px;top:378px;width:228px;font-size:9.5px;line-height:13.5px;color:#e4e4e4}
.btn-outline{position:absolute;left:229px;top:464px;width:136px;height:34px;border:2px solid var(--lime);color:var(--white);font-size:11px;font-weight:700;display:flex;align-items:center;justify-content:center;letter-spacing:.5px}
.dots{position:absolute;left:563px;top:538px;display:flex;gap:11px}
.dots span{width:13px;height:13px;border:2px solid var(--white);border-radius:50%}

/* Trust */
.trust{position:absolute;left:0;top:577px;width:1200px;height:432px;background:var(--ink)}
.trust-title{position:absolute;left:0;width:1200px;top:58px;text-align:center;font-size:21px;font-weight:500;color:var(--white)}
.trust-lead{position:absolute;left:290px;width:620px;top:112px;text-align:center;font-size:11.5px;line-height:17px;color:var(--lime)}
.feature{position:absolute;top:207px;width:230px;height:160px;border:2px solid #6f9f48;text-align:center;color:var(--white)}
.feature svg{display:block;margin:22px auto 0}
.feature h3{margin-top:10px;font-size:13px;font-weight:500;color:var(--lime)}
.feature p{margin:8px auto 0;width:196px;font-size:9.5px;line-height:13.5px;color:#d8d8d8}

/* Services */
.services{position:absolute;left:0;top:1009px;width:1200px;height:950px;background:var(--paper)}
.services-lead{position:absolute;left:0;width:1200px;top:45px;text-align:center;font-size:19px;line-height:32px;color:var(--text-dark)}
.tile{position:absolute;width:400px;height:346px}
.tile-label{position:absolute;left:73px;top:210px;width:252px;height:85px;border:2px solid #2e3a1f;display:flex;flex-direction:column;align-items:center;justify-content:center;font-size:26px;line-height:31px;color:#2e3a1f;letter-spacing:1px}
.loading{position:absolute;left:0;width:1200px;top:864px;text-align:center;font-size:13px;color:#333}
.loading-dots{position:absolute;left:568px;top:893px;display:flex;gap:13px}
.loading-dots span{width:12px;height:12px;border-radius:50%}

/* Contact */
.contact{position:absolute;left:0;top:1959px;width:1200px;height:529px;background:linear-gradient(180deg,#2c2a3c 0%,#34324a 60%,#2e2c40 100%)}
.contact-title{position:absolute;left:0;width:1200px;top:48px;text-align:center;font-size:19px;font-weight:600;color:var(--lime)}
.contact-intro{position:absolute;left:157px;top:118px;width:330px;font-size:9.5px;line-height:17px;color:#e2e2e8}
.field{position:absolute;background:var(--field);font-size:9.5px;color:#444;padding:8px 9px}
.btn-violet{position:absolute;left:376px;top:425px;width:136px;height:41px;background:var(--violet);color:var(--white);font-size:11px;font-weight:600;display:flex;align-items:center;justify-content:center}
.info{position:absolute;left:688px;color:var(--white);display:flex;gap:16px;align-items:flex-start}
.info-phone{top:168px;font-size:20px;font-weight:500}
.info-mail{top:220px;font-size:15px}
.info-address{top:270px;font-size:15px;line-height:27px}

/* Footer */
.footer{position:absolute;left:0;top:2488px;width:1200px;height:92px;background:var(--ink-deep)}
.brand-foot{left:155px;top:24px;font-size:32px;line-height:36px;color:var(--white)}
.nav-foot{left:0;top:38px;font-size:16px}
.legal{position:absolute;left:0;top:2580px;width:1200px;height:67px;background:var(--bar)}
.copyright{position:absolute;left:155px;top:24px;font-size:14px;color:var(--muted)}
.social{position:absolute;top:17px;width:32px;height:32px;border-radius:4px;background:#6e6e74}
</style>
</head>
<body>

<section class="hero">
  <div class="abs" role="img" aria-label="Technician in a hard hat and safety glasses servicing rooftop air conditioning units" style="inset:0"></div>
  <div class="hero-shade"></div>
  <header class="topbar">
    <div class="brand brand-top">BRISK</div>
    <nav class="nav nav-top">
      <a style="left:0">Home</a>
      <a style="left:76px">About</a>
      <a style="left:154px">Services</a>
      <a style="left:251px">Contact Us</a>
    </nav>
  </header>
  <h1 class="hero-title">KNOWLEDGE.<br><span class="accent">EXPERIENCE.</span><br>PASSION.</h1>
  <p class="hero-copy">Commercial cooling experts on call around the clock. We service cold rooms, display cabinets and air conditioning across Joondalup and the wider Perth Metro area, keeping your business running cool.</p>
  <div class="btn-outline">BOOK NOW</div>
  <div class="dots"><span></span><span></span><span></span><span></span></div>
</section>

<section class="trust">
  <h2 class="trust-title">Most Trusted Commercial Refrigeration &amp; AC Specialists</h2>
  <p class="trust-lead">Our experienced and highly trained technicians provide extensive knowledge and exceptional skills for your commercial refrigeration and air conditioning requirements.</p>

  <div class="feature" style="left:224px">
    <svg width="30" height="30" viewBox="0 0 30 30" fill="none" stroke="#dcdcdc" stroke-width="1.6"><circle cx="15" cy="15" r="12"/><path d="M15 8v7l-4 4"/></svg>
    <h3>Open 24/7 - Available</h3>
    <p>Emergency repair services 24 hours a day, seven days a week. Brisk is always ready to repair &amp; support.</p>
  </div>
  <div class="feature" style="left:480px">
    <svg width="32" height="30" viewBox="0 0 32 30" fill="none" stroke="#dcdcdc" stroke-width="1.6"><path d="M16 27 4 15a7 7 0 0 1 12-9 7 7 0 0 1 12 9z"/></svg>
    <h3>Satisfaction Guaranteed</h3>
    <p>Brisk offers 100% satisfaction guarantees on all Air-conditioner &amp; Heating services.</p>
  </div>
  <div class="feature" style="left:745px">
    <svg width="30" height="30" viewBox="0 0 30 30" fill="none" stroke="#dcdcdc" stroke-width="1.6"><circle cx="15" cy="15" r="12"/><circle cx="15" cy="12" r="4.5"/><path d="M8 24c1.5-4 4-5.5 7-5.5s5.5 1.5 7 5.5"/></svg>
    <h3>Professional Technicians</h3>
    <p>Our technicians have your safety, welfare and comfort in mind at all times, they are certified and experienced.</p>
  </div>
</section>

<section class="services">
  <p class="services-lead">Brisk Refrigeration's dedicated team specialises in commercial refrigeration<br>and air conditioning equipment.</p>

  <div class="tile" role="img" aria-label="Technician checking gauges on a commercial condenser unit" style="left:0;top:147px;background:linear-gradient(135deg,#8a9aa8,#3f4a5c)"></div>
  <div class="tile" role="img" aria-label="Technician wiring refrigeration controls under a lime overlay" style="left:400px;top:147px;background:linear-gradient(135deg,#b3ea7d,#9ddc62)">
    <div class="tile-label"><span>REFRIGERATION</span><span>REPAIR</span></div>
  </div>
  <div class="tile" role="img" aria-label="Hand adjusting a pressure gauge with a wrench" style="left:800px;top:147px;background:linear-gradient(135deg,#6d6f8a,#c9c3b8 55%,#7b5a4a)"></div>
  <div class="tile" role="img" aria-label="Two technicians in hard hats working on an electrical panel" style="left:0;top:493px;background:linear-gradient(135deg,#9a8a74,#4d5057)"></div>
  <div class="tile" role="img" aria-label="Technician in a blue hard hat servicing an air conditioning unit" style="left:400px;top:493px;background:linear-gradient(135deg,#a7b6c4,#5d6670)"></div>
  <div class="tile" role="img" aria-label="Technician testing a commercial unit with a multimeter" style="left:800px;top:493px;background:linear-gradient(135deg,#c8cdd6,#6e7890)"></div>

  <div class="loading">Loading</div>
  <div class="loading-dots">
    <span style="background:#333"></span><span style="background:#b6b6bc"></span><span style="background:#7e6f9f"></span>
  </div>
</section>

<section class="contact">
  <div class="abs" role="img" aria-label="Faint city skyline behind the booking form" style="inset:0;background:linear-gradient(180deg,rgba(70,68,92,.25),rgba(40,38,56,.1))"></div>
  <h2 class="contact-title">Book for a visit Now!</h2>
  <p class="contact-intro">To request an appointment with Daniel, please provide your contact information by filling out the form below</p>
  <div class="field" style="left:155px;top:173px;width:170px;height:29px">Your Name</div>
  <div class="field" style="left:351px;top:173px;width:161px;height:29px">Phone</div>
  <div class="field" style="left:155px;top:233px;width:170px;height:30px">Your Email</div>
  <div class="field" style="left:351px;top:233px;width:161px;height:30px">Date &nbsp; ___ / ___ / ___</div>
  <div class="field" style="left:155px;top:291px;width:357px;height:106px">Message</div>
  <div class="btn-violet">Send Message</div>

  <div class="info info-phone">
    <svg width="20" height="22" viewBox="0 0 20 22" fill="var(--lime)"><path d="M5 1 8 6 6 8c1 3 3 5.5 6 7l2-2 5 3-2 4C9 19 2 11 1 4z"/></svg>
    <span>630-555-0142</span>
  </div>
  <div class="info info-mail">
    <svg width="20" height="16" viewBox="0 0 20 16"><rect x="1" y="1" width="18" height="14" fill="var(--lime)"/><path d="M1 1l9 7 9-7" fill="none" stroke="#2e2c40" stroke-width="1.5"/></svg>
    <span>hello@briskcooling.example</span>
  </div>
  <div class="info info-address">
    <svg width="20" height="26" viewBox="0 0 20 26" fill="var(--lime)"><path d="M10 1a8 8 0 0 1 8 8c0 6-8 16-8 16S2 15 2 9a8 8 0 0 1 8-8z"/><circle cx="10" cy="9" r="3" fill="#2e2c40"/></svg>
    <span>27 Coldwater Road<br>Joondalup<br>Perth Metro 6027</span>
  </div>
</section>

<footer class="footer">
  <div class="brand brand-foot">BRISK</div>
  <nav class="nav nav-foot">
    <a style="left:671px">Home</a>
    <a style="left:755px">About Us</a>
    <a style="left:865px">Services</a>
    <a style="left:967px">Contact Us</a>
  </nav>
</footer>
<div class="legal">
  <p class="copyright">Copyright © Northgate Web Studio. All rights reserved.</p>
  <span class="social" style="left:914px"></span>
  <span class="social" style="left:962px"></span>
  <span class="social" style="left:1011px"></span>
</div>

</body>
</html>
```